Billboard design 8x3M NURA (Spanish company)

We´re located in the south of Spain. We run a local telecom company.
We sell Fiber optic, and mobile phone lines mainly.
The billboard will have to be in Spanish, I would like the price to be something you spot on first sight when passing by in the car.
Our company color is blue, like in our logo which I will add. I will also add a example from what we currently have.
The new offer should be:
1000 megas + 100Gigas movil con llamadas ilimitadas. (meaning 1000Mb fiber optic speed and 100Gb data and unlimited calls for 1 mobile line)
Our details are: phone line 952 00 0147
Website: nu-ra.es

```html
<!DOCTYPE html>
<html lang="es">
<head>
<meta charset="utf-8">
<title>NURA – Valla 8x3 Fibra Óptica</title>
<link rel="stylesheet" href="https://fonts.googleapis.com/css2?family=Anton&family=Poppins:wght@500;600;700;800&display=swap">
<style>
  :root {
    --stage: #141414;
    --blue-deep: #0f3a55;
    --blue-mid: #1d6f9a;
    --blue-bright: #33aee3;
    --navy: #1c4460;
    --yellow: #e3ad2f;
    --white: #ffffff;
    --ink: #1b3f5a;
    --sliver: #2d8fc4;
  }
  html, body {
    margin: 0;
    width: 1200px;
    height: 800px;
    overflow: hidden;
    background: var(--stage);
  }
  .billboard {
    position: absolute;
    left: 30px;
    top: 170px;
    width: 1140px;
    height: 460px;
    overflow: hidden;
    background: linear-gradient(100deg, var(--blue-deep) 0%, var(--blue-mid) 45%, var(--blue-bright) 100%);
    font-family: "Poppins", sans-serif;
  }
  .bottom-bands {
    position: absolute;
    left: 0;
    top: 0;
    width: 1140px;
    height: 460px;
  }
  .visual {
    position: absolute;
    border-radius: 14px;
  }
  .visual--person {
    left: 87px; top: 60px; width: 328px; height: 310px;
    background: radial-gradient(ellipse at 50% 60%, rgba(150,140,135,.55), rgba(90,75,60,.25) 60%, transparent 75%);
  }
  .visual--wifi-small {
    left: 60px; top: 50px; width: 67px; height: 68px;
    background: radial-gradient(circle at 50% 60%, rgba(220,90,200,.55), rgba(120,80,230,.2) 70%, transparent);
  }
  .visual--wifi-large {
    left: 330px; top: 124px; width: 128px; height: 131px;
    background: radial-gradient(circle at 50% 60%, rgba(230,100,200,.6), rgba(110,80,230,.25) 70%, transparent);
  }
  .visual--rocket-laptop {
    left: 897px; top: 122px; width: 226px; height: 239px;
    background: linear-gradient(180deg, rgba(200,60,50,.35) 0%, rgba(240,150,60,.45) 50%, rgba(220,225,230,.55) 100%);
  }
  .headline {
    position: absolute;
    left: 298px;
    top: 34px;
    margin: 0;
    color: var(--white);
    font-weight: 700;
    font-size: 58px;
    letter-spacing: -1px;
    line-height: 1.2;
    white-space: nowrap;
  }
  .price-tag {
    position: absolute;
    left: 722px;
    top: 10px;
    width: 118px;
    height: 118px;
    border-radius: 50%;
    background: var(--white);
    color: var(--ink);
    display: flex;
    flex-direction: column;
    align-items: center;
    justify-content: center;
    line-height: 1;
  }
  .price-tag__amount {
    font-family: "Anton", sans-serif;
    font-size: 36px;
  }
  .price-tag__period {
    font-weight: 700;
    font-size: 16px;
    margin-top: 4px;
  }
  .price-box {
    position: absolute;
    left: 482px;
    top: 133px;
    width: 350px;
    height: 104px;
    border-radius: 12px;
    background: var(--yellow);
    display: flex;
    align-items: center;
    justify-content: center;
  }
  .price-box__text {
    font-family: "Anton", sans-serif;
    font-size: 66px;
    color: var(--ink);
    line-height: 1;
    letter-spacing: 0.5px;
  }
  .offer-extra {
    position: absolute;
    left: 485px;
    top: 236px;
    margin: 0;
    color: var(--white);
    font-weight: 600;
    font-size: 47px;
    line-height: 1.3;
    white-space: nowrap;
  }
  .offer-note {
    position: absolute;
    left: 484px;
    top: 304px;
    margin: 0;
    color: var(--white);
    font-weight: 500;
    font-size: 31px;
    line-height: 1.2;
    white-space: nowrap;
  }
  .brand {
    position: absolute;
    left: 936px;
    top: 22px;
    width: 170px;
    text-align: center;
    color: var(--white);
  }
  .brand__name {
    display: block;
    font-weight: 700;
    font-size: 46px;
    line-height: 1.1;
    letter-spacing: 2px;
  }
  .brand__services {
    display: block;
    font-weight: 600;
    font-size: 13px;
  }
  .call-now {
    position: absolute;
    left: 60px;
    top: 372px;
    margin: 0;
    color: var(--ink);
    font-weight: 800;
    font-size: 56px;
    line-height: 1.4;
    letter-spacing: -1px;
    white-space: nowrap;
  }
  .website {
    position: absolute;
    left: 767px;
    top: 392px;
    margin: 0;
    color: var(--white);
    font-weight: 700;
    font-size: 44px;
    line-height: 1.35;
    white-space: nowrap;
  }
</style>
</head>
<body>
  <main class="billboard">
    <svg class="bottom-bands" viewBox="0 0 1140 460" aria-hidden="true">
      <polygon points="716,387 1140,387 1140,460 686,460" fill="var(--sliver)"/>
      <polygon points="0,370 716,370 688,460 0,460" fill="var(--yellow)"/>
      <polygon points="742,387 1140,387 1140,460 712,460" fill="var(--navy)"/>
    </svg>

    <div class="visual visual--wifi-small" role="img" aria-label="Icono wifi en 3D de colores rosa y violeta"></div>
    <div class="visual visual--person" role="img" aria-label="Joven sonriente celebrando sentada en un puf con un portátil"></div>
    <div class="visual visual--wifi-large" role="img" aria-label="Icono wifi grande en 3D de colores naranja, rosa y violeta"></div>
    <div class="visual visual--rocket-laptop" role="img" aria-label="Cohete despegando desde la pantalla de un portátil"></div>

    <h1 class="headline">FIBRA ÓPTICA</h1>

    <div class="price-tag">
      <span class="price-tag__amount">39,90€</span>
      <span class="price-tag__period">/mes</span>
    </div>

    <div class="price-box">
      <span class="price-box__text">1000 MEGAS</span>
    </div>
    <p class="offer-extra">+ 100Gigas Movil</p>
    <p class="offer-note">con llamadas ilimitadas.</p>

    <div class="brand">
      <span class="brand__name">NURA</span>
      <span class="brand__services">Wifi | Fibra | Movil | Tv</span>
    </div>

    <p class="call-now">Llama ya : 952 00 0147</p>
    <p class="website">www.nu-ra.es</p>
  </main>
</body>
</html>
```